Bauträger  sucht Webdesign
Bauträger sucht Webdesign
Zielgruppe
Wir sind Bauträger in Öhringen und erstellen Einfamilienhäuser, Mehrfamilienhäuser und Reihenhäuser. Als LM-Hausbau gehen wir gerne auf die individuellen Wünsche unserer Kunden ein. Wir planen sowohl für die junge Familie, als auch für reifere Kunden, mit altersgerechtem Anspruch an die Hausgestaltung.
Aufgabenstellung
Unsere Homepage muss ein moderneres Escheinungsbild bekommen. Unser Logo soll als betongrau /silberne Grafik eingebunden werden. Inhaltlich soll der interessierte Besucher primär schnell eine ansprechende Auswahl haben, um seinen individuellen Vorstellungen näher zu kommen.

```html
<!DOCTYPE html>
<html lang="de">
<head>
<meta charset="utf-8">
<title>LM-Hausbau – Typenhäuser</title>
<link href="https://fonts.googleapis.com/css2?family=Oswald:wght@300;400;600;700&family=Lato:wght@400;700&display=swap" rel="stylesheet">
<style>
:root{
  --sidebar:#1b1b1b;
  --footer:#202020;
  --gold:#c99f06;
  --ink:#1e1e1e;
  --text:#4a4a4a;
  --white:#ffffff;
}
*{box-sizing:border-box;margin:0;padding:0}
html,body{width:1200px;height:3196px;overflow:hidden;background:var(--white)}
body{position:relative;font-family:'Lato',sans-serif;color:var(--text)}
.sidebar{position:absolute;left:0;top:0;width:290px;height:3196px;background:linear-gradient(180deg,#222 0%,#181818 40%,#1c1c1c 100%)}
.brand{position:absolute;left:58px;top:70px;display:flex;align-items:center;gap:10px;font-family:'Oswald',sans-serif;font-weight:600;font-size:24px;color:#bfbfbf;letter-spacing:.5px}
.brand-mark{width:16px;height:16px;background:#bfbfbf}
.nav{position:absolute;left:82px;top:202px;list-style:none}
.nav li{font-family:'Oswald',sans-serif;font-weight:600;font-size:16px;color:var(--white);height:41.3px;line-height:22px;text-transform:uppercase}
.nav li.sub{padding-left:18px;color:var(--gold)}
.hero{position:absolute;left:290px;top:0;width:910px;height:385px;background:linear-gradient(180deg,#9fb6c9 0%,#c9d6cf 45%,#6f8a4f 78%,#4f6a35 100%)}
.intro{position:absolute;left:370px;top:436px;width:620px}
.page-title{font-family:'Oswald',sans-serif;font-weight:700;font-size:46px;line-height:56px;color:var(--ink)}
.page-sub{font-family:'Oswald',sans-serif;font-weight:400;font-size:33px;line-height:40px;color:var(--gold)}
.intro p{font-size:12.5px;line-height:18px;margin-top:18px;width:620px}
.intro p:first-of-type{margin-top:36px}
.link{color:var(--gold)}
.type{position:absolute;left:370px;width:830px}
.type-rule{width:771px;height:4px;background:var(--gold)}
.type-title{font-family:'Oswald',sans-serif;font-weight:600;font-size:34px;line-height:40px;color:var(--ink);margin-top:12px}
.type-body{position:absolute;left:0;width:345px}
.type-lead{font-family:'Oswald',sans-serif;font-weight:300;font-size:21px;line-height:32px;color:var(--ink);text-transform:uppercase;margin-bottom:14px;white-space:nowrap}
.type-body p{font-size:12.2px;line-height:18px;margin-bottom:18px}
.photo{position:absolute;left:381px;width:449px;height:390px}
.plans{position:absolute;left:381px;height:170px;background:linear-gradient(90deg,#d9c58f,#b9b9b9 40%,#d6c189 70%,#c9b27a)}
.footer{position:absolute;left:290px;top:2948px;width:910px;height:219px;background:var(--footer)}
.footer-bar{position:absolute;left:290px;top:3167px;width:910px;height:29px;background:var(--gold);font-size:10px;color:var(--ink);text-align:right;padding-right:59px;line-height:29px;word-spacing:8px}
.f-col{position:absolute;top:48px;color:var(--white);font-size:12px;line-height:18px}
.f-head{font-family:'Oswald',sans-serif;font-size:17px;font-weight:400;margin-bottom:10px;line-height:22px}
.hours{border-collapse:collapse}
.hours td{padding:0 14px 9px 0;font-size:12px;line-height:18px}
.badge{position:absolute;top:76px;width:66px;height:66px;border-radius:50%;border:3px solid var(--white)}
</style>
</head>
<body>
<aside class="sidebar">
  <div class="brand"><span class="brand-mark"></span>LM-Hausbau</div>
  <ul class="nav">
    <li>Start</li><li>Das sind wir</li><li>Aktuelles</li><li>Archiv</li>
    <li class="sub">Typenhäuser</li>
    <li>Referenzen</li><li>Impressionen</li><li>Kontakt</li>
  </ul>
</aside>

<div class="hero" role="img" aria-label="Modernes weißes Einfamilienhaus mit Terrasse, Sonnenschirm und Garten"></div>

<section class="intro">
  <h1 class="page-title">TYPENHÄUSER</h1>
  <h2 class="page-sub">Schnell zu Ihrem Traumhaus</h2>
  <p>Mit einem Modellhaustyp aus unserem <span class="link">Hauskatalog</span> bieten wir Ihnen die Möglichkeit schnell Ihr<br>Traumhaus zu finden. Hier sind die Häuser komplett geplant und je nach Ausstattung mit einem Festpreis<br>versehen. So lässt sich der Traum vom eigenen Heim in die Wirklichkeit umzusetzen.</p>
  <p>Gern beziehen wir Ihre individuellen Wünsche bei jeder Planung und Gestaltung mit ein, so dass Sie in<br>Ihrem ganz persönlich geplanten Haus wohnen werden.<br>Für kostenbewusste Bauherren werden <span class="link">weitere verschiedene Modellhaustypen</span> in einem Hauskatalog<br>angeboten.</p>
</section>

<section class="type" style="top:820px">
  <div class="type-rule"></div>
  <h2 class="type-title">TYP 1 - PURISMUS</h2>
  <div class="type-body" style="top:84px">
    <h3 class="type-lead">Modernes Ambiente für die An-<br>sprüche von heute.</h3>
    <p>Liebhaber von puristisch-eleganter Architektur- und Formensprache werden sich in diesem Haus mehr als nur wohl fühlen. Sowohl in der äußeren Erscheinung als auch der Raumaufteilung besticht das Objekt durch zeitlose Klarheit.</p>
    <p>Besonders hervorstechend sind die großzügig bemessenen Freiflächen: Gleich zwei Balkone im 1. Obergeschoss sowie die Terrasse im Erdgeschoss lassen reichlich Raum zur Entfaltung und viel Platz für erholsame Stunden im Freien.</p>
    <p>Doch auch im Inneren bleiben keine Wünsche offen. Ihre persönlichen Vorstellungen sind unser Anspruch: Sie können Details noch frei mitplanen und entscheiden, Zimmer zusammenlegen oder trennen, eine offene oder geschlossene Küche wählen u.v.m.</p>
    <p>Abgerundet wird das durchdachte Objekt durch die direkt am Haus befindliche Einzelgarage, sowie sie in der Architektur integrierte Eingangsüberdachung.</p>
  </div>
  <div class="photo" style="top:87px;background:linear-gradient(180deg,#d9e6ef 0%,#f2f2f2 50%,#7c9a4c 85%)" role="img" aria-label="Visualisierung Typ Purismus: kubisches weißes Haus mit Garage"></div>
  <div class="plans" style="top:509px;width:420px" role="img" aria-label="Grundrisse der Geschosse Typ Purismus"></div>
</section>

<section class="type" style="top:1574px">
  <div class="type-rule"></div>
  <h2 class="type-title">TYP 3 - STIL</h2>
  <div class="type-body" style="top:84px">
    <h3 class="type-lead">Der extravagante Grundriss für<br>besondere Ansprüche.</h3>
    <p>Stilvoll und repräsentativ: So mutet dieses Objekt an für Kunden der besonderen Ansprüche. Die deckenhohen Fensterfronten des Erd- und Obergeschosses tragen das ihre zum harmonischen äußeren Gesamtbild bei. Und verleihen selbstverständlich jedem einzelnen Raum enorme Helligkeit, die Sie bald schon nicht mehr missen möchten.</p>
    <p>Die gelungene Dachform mit leichtem Versatz ist eines von vielen weiteren exquisiten Details, die dieses Haus zu etwas ganz Besonderem machen.</p>
    <p>Im Wohnbereich wurde Wert gelegt auf ein Raumangebot, das allen Wünschen gerecht wird. Offenheit, Großzügigkeit und viel Spielraum zum Ausleben individueller Vorlieben kennzeichnen die gesamte Wohnfläche auf guten 170 Quadratmetern.</p>
  </div>
  <div class="photo" style="top:88px;background:linear-gradient(180deg,#6d9bd0 0%,#b9cde0 30%,#eeeeee 55%,#7ea24e 85%)" role="img" aria-label="Visualisierung Typ Stil: weißes Haus mit rotem Satteldach"></div>
  <div class="plans" style="top:580px;width:393px;height:166px" role="img" aria-label="Grundrisse der Geschosse Typ Stil"></div>
</section>

<section class="type" style="top:2393px">
  <div class="type-rule"></div>
  <h2 class="type-title">TYP 5 - ELEGANZ</h2>
  <div class="type-body" style="top:84px">
    <h3 class="type-lead">Moderne Akzente schaffen: Hoch-<br>wertigkeit und Eleganz.</h3>
    <p>Die Herzen aller Frauen schlagen höher bei der Möglichkeit eines begehbaren Kleiderschranks. Dies stellt nur einen von vielen Glanzpunkten des Objekts dar und ist auf clevere Weise realisiert: Die Ankleide im OG kann sowohl vom Schlafzimmer als auch vom Bad her erreicht werden.</p>
    <p>Das Erdgeschoss hält ein nicht minder reizvolles Highlight bereit: den beheizten Wintergarten mit direktem Anschluss zur Terrasse. So müssen Sie in den kalten Monaten nicht auf wärmende Sonnenstrahlen verzichten, sondern können Licht und Kraft tanken für den Alltag – zu jeder Zeit.</p>
    <p>Im äußeren Erscheinungsbild ist die klassische Eleganz nicht von der Hand zu weisen und zieht sich in allen optischen Elementen des Objekts geradlinig durch.</p>
  </div>
  <div class="photo" style="top:88px;background:linear-gradient(180deg,#7fb0de 0%,#cfdde9 35%,#ececec 60%,#7fa14d 88%)" role="img" aria-label="Visualisierung Typ Eleganz: weißes Haus mit dunklem Satteldach"></div>
</section>

<footer class="footer">
  <div class="f-col" style="left:80px">
    <div class="f-head">LM-HAUSBAU GMBH</div>
    Am Lindenhang 7<br>74599 Brunnweiler<br>Tel. 07950-5520-0<br>info@lm-hausbau.de
  </div>
  <div class="f-col" style="left:288px">
    <div class="f-head">ÖFFNUNGSZEITEN</div>
    <table class="hours">
      <tr><td>Mo. bis Fr.</td><td>von 08:30 Uhr bis 12:30 Uhr</td></tr>
      <tr><td>Mo. bis Do.</td><td>von 13:30 Uhr bis 18:00 Uhr</td></tr>
      <tr><td>Freitag</td><td>von 13:30 Uhr bis 16:00 Uhr</td></tr>
    </table>
    sowie nach Vereinbarung
  </div>
  <div class="badge" style="left:679px" role="img" aria-label="Qualitätssiegel"></div>
  <div class="badge" style="left:787px" role="img" aria-label="Verbandssiegel"></div>
</footer>
<div class="footer-bar">HOME SITEMAP IMPRESSUM DATENSCHUTZ</div>
</body>
</html>
```